Briefpapier für Träger der Familienhilfe
Sie geht auf alle Wünsche sehr schnell ein!! Sehr gute Zusammenarbeit! Danke
Zielgruppe
Wir sind ein Träger der Familienhilfe und bieten Hilfen zur Erziehung an. Unsere Auftraggeber sind die Jugendämter in Hamburg. Unsere Zielgruppe sind Familien/Einzelpersonen in Krisensituationen.
Aufgabenstellung
Wir möchten, dass unser Logo in das Design integriert wird. Da der Briefverkehr hauptsächlich mit Behörden, Ämtern, Schulen etc. stattfinden wird, ist es wichtig, dass wir einen seriösen Eindruck machen.

```html
<!DOCTYPE html>
<html lang="de">
<head>
<meta charset="utf-8">
<title>Briefpapier – Lindenweg Familienhilfe</title>
<link rel="stylesheet" href="https://fonts.googleapis.com/css2?family=Noto+Sans:wght@400;700&display=swap">
<style>
  :root {
    --ink: #000000;
    --paper: #ffffff;
    --brand-green: #9acd32;
    --brand-green-soft: rgba(154, 205, 50, 0.55);
    --brand-green-fade: rgba(154, 205, 50, 0);
    --brand-grey: #8c8c8c;
    --rule: 2px solid var(--ink);
  }
  * { margin: 0; padding: 0; box-sizing: border-box; }
  html, body {
    width: 849px;
    height: 1200px;
    overflow: hidden;
    background: var(--paper);
  }
  body {
    font-family: "Noto Sans", sans-serif;
    color: var(--ink);
  }
  .letterhead {
    position: relative;
    width: 849px;
    height: 1200px;
    overflow: hidden;
    background: var(--paper);
  }
  .letterhead > * { position: absolute; z-index: 1; }

  .corner-tint {
    z-index: 0;
    right: 0;
    bottom: 0;
    width: 849px;
    height: 660px;
    background:
      radial-gradient(ellipse 95% 90% at 100% 100%,
        var(--brand-green) 0%,
        var(--brand-green-soft) 40%,
        var(--brand-green-fade) 100%);
  }

  .sender-line {
    left: 82px;
    top: 163px;
    font-size: 12px;
    font-weight: 700;
    text-decoration: underline;
  }

  .brand {
    right: 58px;
    top: 66px;
    display: flex;
    align-items: center;
    gap: 12px;
  }
  .brand-dot {
    width: 26px;
    height: 26px;
    border-radius: 50%;
    background: var(--brand-green);
    flex: none;
  }
  .brand-name {
    font-size: 24px;
    font-weight: 400;
    line-height: 1.15;
    color: var(--brand-grey);
  }

  .sender-address {
    right: 59px;
    top: 175px;
    font-size: 21.5px;
    line-height: 25px;
    font-style: normal;
    text-align: center;
  }

  .subject {
    left: 82px;
    top: 340px;
    font-size: 25px;
    font-weight: 700;
  }

  .reference-table {
    left: 20px;
    top: 390px;
    width: 803px;
    height: 43px;
    border-collapse: collapse;
    font-size: 20px;
  }
  .reference-table td {
    border: var(--rule);
    vertical-align: top;
    padding: 0 0 0 9px;
    line-height: 24px;
  }
  .reference-table td:first-child { padding-left: 1px; width: 206px; }
  .reference-table td:nth-child(2) { width: 185px; }
  .reference-table td:nth-child(3) { width: 144px; }

  .footer-rule {
    left: 20px;
    top: 1108px;
    width: 802px;
    border-top: var(--rule);
  }
  .legal-info {
    left: 21px;
    top: 1119px;
    font-size: 22px;
    line-height: 25px;
  }
</style>
</head>
<body>
<main class="letterhead">
  <div class="corner-tint" role="img" aria-label="Sanfter grüner Farbverlauf als Hintergrundakzent unten rechts"></div>

  <p class="sender-line">Lindenweg Familienhilfe, Musterstrasse 12, 01234 Hamburg</p>

  <div class="brand">
    <span class="brand-dot"></span>
    <span class="brand-name">Lindenweg<br>Familienhilfe</span>
  </div>

  <address class="sender-address">
    Musterstrasse 12<br>01234 Hamburg
  </address>

  <h1 class="subject">Betreff:</h1>

  <table class="reference-table">
    <tr>
      <td>Unser Zeichen</td>
      <td>Durchwahl</td>
      <td>Zimmer</td>
      <td>Ansprechpartner</td>
    </tr>
  </table>

  <div class="footer-rule"></div>
  <p class="legal-info">
    Rechtliche Informationen:<br>
    Inhaber, Bankdaten falls erforderlich, Steuernummer usw. finden hier Platz
  </p>
</main>
</body>
</html>
```